Wedding Invitations

We are a printing company "inkmorrow" and require multiple wedding invitation designs for our customers in store and online. We would like the designs to be editable in Photoshop if possible, if not then a layout with suggested fonts would be the next best option. We are open to suggestions on design but would like to stick to the general wedding themes some with a modern and some with a classical feel

Industry/Entity Type

Printing

```html
<!DOCTYPE html>
<html lang="en">
<head>
<meta charset="utf-8">
<title>Wedding Invitation – Caroline and James</title>
<link rel="stylesheet" href="https://fonts.googleapis.com/css2?family=Lobster+Two:wght@400;700&family=Poiret+One&display=swap">
<style>
  :root {
    --gold: #fccb1d;
    --paper: #ffffff;
    --ink-dark: #2a2c10;
    --ink-slate: #56605f;
    --ink-pale: #c6cfcc;
  }
  html, body {
    margin: 0;
    padding: 0;
    width: 1200px;
    height: 862px;
    overflow: hidden;
    background: var(--paper);
  }
  .invitation {
    display: block;
    width: 1200px;
    height: 862px;
  }
  .band { fill: var(--gold); }
  .ornament { fill: var(--gold); }
  .hosts {
    font-family: "Lobster Two", cursive;
    font-size: 170px;
    fill: var(--ink-dark);
  }
  .request, .details {
    font-family: "Poiret One", sans-serif;
    font-size: 50px;
    word-spacing: 8px;
    fill: var(--ink-slate);
  }
  .couple {
    font-family: "Lobster Two", cursive;
    font-weight: 400;
    font-size: 190px;
    fill: var(--ink-slate);
  }
  .time {
    font-family: "Poiret One", sans-serif;
    font-size: 50px;
    word-spacing: 8px;
    fill: var(--ink-pale);
  }
</style>
</head>
<body>
<svg class="invitation" viewBox="0 0 1200 862" xmlns="http://www.w3.org/2000/svg">
  <rect class="band band--top" x="0" y="0" width="1200" height="28"/>
  <rect class="band band--bottom" x="0" y="833" width="1200" height="29"/>

  <text class="hosts" x="20" y="200" textLength="1155" lengthAdjust="spacingAndGlyphs">Thomas and Eleanor Hartley &amp; Robert and Margaret Lowell</text>

  <text class="request" x="85" y="283" textLength="1028" lengthAdjust="spacing">Request the honor of your presence at the marriage of their children</text>

  <path class="band rule rule--upper-left" d="M0 350 C20 356 40 358 70 358 L540 358 L540 361 L70 362 C40 362 20 366 0 372 Z"/>
  <path class="band rule rule--upper-right" d="M1200 350 C1180 356 1160 358 1130 358 L665 358 L665 361 L1130 362 C1160 362 1180 366 1200 372 Z"/>
  <path class="band rule rule--lower" d="M0 522 C20 530 45 533 75 533 L1125 533 C1155 533 1180 530 1200 522 L1200 548 C1180 540 1155 537 1125 537 L75 537 C45 537 20 540 0 548 Z"/>

  <rect class="ornament" x="556" y="298" width="86" height="98" rx="24" role="img" aria-label="Gold fleur-de-lis ornament"/>

  <text class="couple" x="62" y="508" textLength="1076" lengthAdjust="spacingAndGlyphs">Caroline and James</text>

  <text class="details details--date" x="58" y="657" textLength="1084" lengthAdjust="spacing">Saturday the fourteenth of September,Two thousand and thirteen</text>
  <text class="details details--venue" x="58" y="735" textLength="550" lengthAdjust="spacing">Willow Garden in Harbor Park.</text>
  <text class="details details--city" x="58" y="808" textLength="334" lengthAdjust="spacing">Mahattan, New York</text>

  <text class="time" x="900" y="738" textLength="238" lengthAdjust="spacing">Four o’clock in</text>
  <text class="time" x="930" y="808" textLength="208" lengthAdjust="spacing">the aftenoon</text>
</svg>
</body>
</html>
```